Hallo liebe Designer,
wir haben bereits ein Design, welches sich an den Farben unserer Homepage www.kbtr.de orientiert. Dieses Design muss nachgebaut werden. Wir benötigen eine editierbare Microsoft-WORD-Datei, die nach Bedarf angepasst werden kann (falls sich Telefonnummer oder ähnliches mal ändert)
Zusammengefasst:
Benötigt wird: Ein Worddokument mit einem Briefpapier mit der Hauptseite und Folgeseiten. Die Folgeseiten sollen automatisch entstehen, wenn mehr wie 1 Seite beschrieben wird.
Das Design bitte so nachbauen wie es im PDF ersichtlich ist.
- das Worddokument muss anpassbar sein, falls sich mal die Telefonnummer o.ä. ändert

```html
<!DOCTYPE html>
<html lang="de">
<head>
<meta charset="utf-8">
<title>KBT Unternehmensgruppe – Briefpapier</title>
<link href="https://fonts.googleapis.com/css2?family=Arimo&family=Jost:wght@400;500&display=swap" rel="stylesheet">
<style>
  :root {
    --backdrop: #a9a8ad;
    --paper: #ffffff;
    --ink: #111111;
    --muted: #8a8d89;
    --brand-light: #a3a9a0;
    --brand-dark: #7b8079;
    --logo: #8e958b;
  }
  * { margin: 0; padding: 0; box-sizing: border-box; }
  html, body { width: 1200px; height: 1200px; overflow: hidden; background: var(--backdrop); }
  .letterhead {
    position: absolute; left: 212px; top: 51px;
    width: 775px; height: 1097px;
    background: var(--paper); overflow: hidden;
  }
  .brand {
    position: absolute; left: 476px; top: 48px;
    font-family: "Jost", sans-serif; font-weight: 500; color: var(--logo);
  }
  .brand-name { display: flex; align-items: center; gap: 10px; font-size: 50px; line-height: 1; letter-spacing: 1px; }
  .brand-dot { width: 22px; height: 22px; border-radius: 50%; background: var(--brand-dark); }
  .brand-sub { margin: 6px 0 0 95px; font-size: 18px; line-height: 1; }
  .letter-body {
    position: absolute; left: 56px; top: 195px; width: 663px;
    font-family: "Arimo", sans-serif; font-size: 13.1px; line-height: 18.2px;
    color: var(--ink); text-align: justify;
  }
  .letter-body p + p { margin: 0; }
  .letter-body .gap { height: 18.2px; }
  .footer-info {
    position: absolute; top: 987px; left: 0; width: 100%;
    font-family: "Jost", sans-serif; font-size: 9.4px; line-height: 12.5px; color: var(--muted);
  }
  .footer-col { position: absolute; top: 0; }
  .footer-col.management { left: 56px; }
  .footer-col.finance { left: 209px; }
  .footer-col.contact { left: 422px; }
  .footer-rule { position: absolute; top: -2px; width: 1.5px; height: 68px; background: var(--muted); }
  .footer-rule.r1 { left: 192px; }
  .footer-rule.r2 { left: 405px; }
  .contact-line { display: flex; align-items: center; }
  .contact-line svg { width: 9px; height: 9px; margin-right: 15px; fill: none; stroke: var(--muted); stroke-width: 1.2; }
  .band { position: absolute; left: 0; bottom: 0; width: 100%; height: 26px; background: var(--brand-light); }
  .band-accent { position: absolute; left: 0; top: 1043px; width: 775px; height: 54px; }
  .web-address {
    position: absolute; left: 612px; top: 1050px;
    font-family: "Jost", sans-serif; font-size: 19px; line-height: 1; color: #ffffff; letter-spacing: 0.3px;
  }
</style>
</head>
<body>
<main class="letterhead">
  <div class="brand">
    <div class="brand-name"><span class="brand-dot"></span>KBT</div>
    <div class="brand-sub">Unternehmensgruppe</div>
  </div>

  <section class="letter-body">
    <p>Sehr geehrter Herr Mustermann, jeder Setzer hat für diesen Zweck immer etwas Blindtext parat. Blindtext ist im Umfang von einigen tausend Anschlägen, der für die »äußerliche« Gestaltung einer Publikation verwendet und dessen Inhalt unwichtig ist. Man setzt ihn oft zum Beispiel in verschiedenen Schriften und Schriftgrößen, um anderen zu zeigen, wie eine bestimmte Schrift wirkt.</p>
    <p>Sehr geehrter Herr Mustermann, jeder Setzer hat für diesen Zweck immer etwas Blindtext parat. Blindtext ist im Umfang von einigen tausend Anschlägen, der für die »äußerliche« Gestaltung einer Publikation verwendet und dessen Inhalt unwichtig ist. Man setzt ihn oft zum Beispiel in verschiedenen Schriften und Schriftgrößen, um anderen zu zeigen, wie eine bestimmte Schrift wirkt.</p>
    <div class="gap"></div>
    <p>Sehr geehrter Herr Mustermann, jeder Setzer hat für diesen Zweck immer etwas Blindtext parat. Blindtext ist im Umfang von einigen tausend Anschlägen, der für die »äußerliche« Gestaltung einer Publikation verwendet und dessen Inhalt unwichtig ist. Man setzt ihn oft zum Beispiel in verschiedenen Schriften und Schriftgrößen, um anderen zu zeigen, wie eine bestimmte Schrift wirkt.</p>
    <p>Sehr geehrter Herr Mustermann, jeder Setzer hat für diesen Zweck immer etwas Blindtext parat. Blindtext ist im Umfang von einigen tausend Anschlägen, der für die »äußerliche« Gestaltung einer Publikation verwendet und dessen Inhalt unwichtig ist. Man setzt ihn oft zum Beispiel in verschiedenen Schriften und Schriftgrößen, um anderen zu zeigen, wie eine bestimmte Schrift wirkt.</p>
    <p>Sehr geehrter Herr Mustermann, jeder Setzer hat für diesen Zweck immer etwas Blindtext parat. Blindtext ist im Umfang von einigen tausend Anschlägen, der für die »äußerliche« Gestaltung einer Publikation verwendet und dessen Inhalt unwichtig ist. Man setzt ihn oft zum Beispiel in verschiedenen Schriften und Schriftgrößen, um anderen zu zeigen, wie eine bestimmte Schrift wirkt.</p>
    <div class="gap"></div>
    <p>Sehr geehrter Herr Mustermann, jeder Setzer hat für diesen Zweck immer etwas Blindtext parat. Blindtext ist im Umfang von einigen tausend Anschlägen, der für die »äußerliche« Gestaltung einer Publikation verwendet und dessen Inhalt unwichtig ist. Man setzt ihn oft zum Beispiel in verschiedenen Schriften und Schriftgrößen, um anderen zu zeigen, wie eine bestimmte Schrift wirkt.</p>
    <p>Sehr geehrter Herr Mustermann, jeder Setzer hat für diesen Zweck immer etwas Blindtext parat. Blindtext ist im Umfang von einigen tausend Anschlägen, der für die »äußerliche« Gestaltung einer Publikation verwendet und dessen Inhalt unwichtig ist. Man setzt ihn oft zum Beispiel in verschiedenen Schriften und Schriftgrößen, um anderen zu zeigen, wie eine bestimmte Schrift wirkt.</p>
    <p>Sehr geehrter Herr Mustermann, jeder Setzer hat für diesen Zweck immer etwas Blindtext parat. Blindtext ist im Umfang von einigen tausend Anschlägen, der für die »äußerliche« Gestaltung einer Publikation verwendet und dessen Inhalt unwichtig ist. Man setzt ihn oft zum Beispiel in verschiedenen Schriften und Schriftgrößen, um anderen zu zeigen, wie eine bestimmte Schrift wirkt.</p>
  </section>

  <footer class="footer-info">
    <div class="footer-col management">
      Geschäftsführung:<br>Markus Lehnert<br>Carina Wolters<br>Amtsgericht Lindenfeld<br>HRB 40718
    </div>
    <span class="footer-rule r1"></span>
    <div class="footer-col finance">
      Umsatzsteuer-ID<br>DE000000000<br>Stadtbank Lindenfeld<br>BIC: STBLDEXXXXX<br>IBAN: DE00 0000 0000 0000 0000 00
    </div>
    <span class="footer-rule r2"></span>
    <div class="footer-col contact">
      Postanschrift:<br>Ahornweg 12<br>12345 Lindenfeld
      <div class="contact-line">
        <svg viewBox="0 0 10 10" aria-hidden="true"><path d="M2 1l2 2-1 1.5c.6 1.2 1.3 1.9 2.5 2.5L7 6l2 2-1.5 1.5C4.5 9 1 5.5.5 2.5z" fill="#8a8d89" stroke="none"/></svg>+49 000 / 12345678
      </div>
      <div class="contact-line">
        <svg viewBox="0 0 10 10" aria-hidden="true"><rect x="0.6" y="1.8" width="8.8" height="6.4"/><path d="M0.6 1.8L5 5.6l4.4-3.8"/></svg>info@kbtr.de
      </div>
    </div>
  </footer>

  <div class="band"></div>
  <svg class="band-accent" viewBox="0 0 775 54" aria-hidden="true">
    <polygon points="548,0 775,0 775,54 514,54" fill="#7b8079"/>
  </svg>
  <div class="web-address">www.kbtr.de</div>
</main>
</body>
</html>
```